Webshop Template

For our Webstore in UK we need a complete Template,
shoppingcart is Magento, the Shop is focussed on Download software,

the name: Appvaultdepot.co.uk

Check out some other good stores, like lumawerk.de

for example the Page from 

www.brenvik.co.uk or

www.lumawerk.de

www.tastenhugo.de

www.klickrabatt.de

The Logodesign which are in Consideration

http://www.artmosaiq.com/design/5520817/logo-design-by-tomasz7kv

http://www.artmosaiq.com/design/5518360/logo-design-by-luisgaviota

http://www.artmosaiq.com/design/5517245/logo-design-by-kestrel-works

http://www.artmosaiq.com/design/5516093/logo-design-by-zumbiloft

http://www.artmosaiq.com/design/5515471/logo-design-by-tivaro

http://www.artmosaiq.com/design/5514902/logo-design-by-blue-fern-graphics-

Target Market(s)

B2C - Consumer Marcet

Industry/Entity Type

Shop

```html
<!DOCTYPE html>
<html lang="en">
<head>
<meta charset="utf-8">
<title>Appvault depot – Webshop</title>
<link href="https://fonts.googleapis.com/css2?family=Lobster&family=Oswald:wght@300;400;700&display=swap" rel="stylesheet">
<style>
:root{
  --page:#ececec;--white:#fff;--ink:#222;--grey:#666;--grey-soft:#999;--line:#ddd;
  --yellow:#f5b820;--yellow-dark:#d99a0c;--blue:#35b5ce;--orange:#f0a81a;--panel:#e2e2e2;
}
*{margin:0;padding:0;box-sizing:border-box}
html,body{width:1000px;height:1200px;overflow:hidden;background:var(--white)}
body{position:relative;font-family:"Oswald",sans-serif;color:var(--grey)}
.abs{position:absolute}
.page{left:65px;top:0;width:895px;height:1200px;background:var(--page)}
.topline{left:65px;top:0;width:895px;height:3px;background:var(--yellow)}
.welcome{right:320px;top:7px;font:700 9.5px Arial,sans-serif;color:#555;white-space:nowrap;text-align:right}
.currency{left:695px;top:0;width:206px;height:20px;background:var(--yellow);border-radius:0 0 3px 3px}
.currency span{position:absolute;left:7px;top:4px;font:700 9px Arial,sans-serif;color:#5a3d00;white-space:nowrap}
.currency .select{position:absolute;left:98px;top:2px;width:105px;height:15px;background:#fff;font:9px Arial,sans-serif;color:#777;padding:2px 4px;white-space:nowrap}
.currency .select i{position:absolute;right:2px;top:2px;width:11px;height:11px;border:1px solid #777;background:#eee}
.logo{left:152px;top:23px;font:700 30px/27px "Oswald",sans-serif;color:#111;letter-spacing:.5px}
.account{right:310px;top:56px;display:flex;font:8px Arial,sans-serif;color:#666;white-space:nowrap}
.account a{padding:0 8px;border-left:1px solid #ccc;text-decoration:none;color:inherit}
.account a:first-child{padding-left:0;border:0}
.account a:last-child{padding-right:0}
.cart{left:705px;top:43px;width:196px;height:34px;background:var(--blue);border-radius:3px;color:#fff;font:10px/12px "Oswald",sans-serif}
.cart svg{position:absolute;left:12px;top:8px}
.cart p{position:absolute;left:46px;top:5px;white-space:nowrap}
.nav{left:123px;top:103px;width:778px;height:46px;background:var(--white);border:1px solid var(--line);display:flex}
.nav a{display:block;height:44px;line-height:44px;padding:0 22px;font-size:12px;color:#444;border-right:1px solid var(--line);text-decoration:none;text-transform:uppercase}
.search{left:694px;top:113px;width:170px;height:24px;background:#e2e2e2;font:300 10px/24px "Oswald",sans-serif;color:#777;padding-left:8px}
.search-btn{left:863px;top:113px;width:28px;height:24px;background:var(--yellow)}
.blueline{left:65px;top:148px;width:895px;height:4px;background:var(--blue)}
.slider{left:123px;top:176px;width:778px;height:382px;background:var(--white)}
.slide{left:130px;top:183px;width:763px;height:367px;background:radial-gradient(ellipse at 30% 50%,#fff 40%,#e8e8e8 100%)}
.photo{background:linear-gradient(160deg,#3a3a3a,#111 60%,#2a6d9a)}
.phone-lg{left:160px;top:262px;width:128px;height:278px;border-radius:14px}
.badge{left:230px;top:226px}
.hero-title{left:305px;top:295px;font:52px "Lobster",cursive;color:#111;white-space:nowrap}
.hero-sub{left:305px;top:350px;font:16px "Oswald",sans-serif;color:var(--orange)}
.hero-body{left:305px;top:375px;width:215px;font:300 12px/15px "Oswald",sans-serif;color:#333}
.btn{background:linear-gradient(#f9c83a,var(--yellow));border:1px solid var(--yellow-dark);border-radius:3px;font:20px "Lobster",cursive;color:#5a3800;text-align:center;white-space:nowrap}
.btn-hero{left:305px;top:434px;width:113px;height:32px;line-height:30px}
.sale-panel{left:543px;top:198px;width:336px;height:336px;background:var(--panel)}
.sale-card{left:559px;top:214px;width:304px;height:305px;background:var(--white);text-align:center}
.sale-word{left:0;top:2px;width:304px;font:110px/120px "Lobster",cursive;color:#666}
.sale-sub{left:0;top:116px;width:304px;font:16px "Oswald",sans-serif;color:var(--orange);white-space:nowrap}
.sale-off{left:0;top:142px;width:304px;font:38px "Lobster",cursive;color:var(--blue)}
.sale-body{left:20px;top:204px;width:264px;font:300 11px/14px "Oswald",sans-serif;color:#555}
.btn-shop{left:100px;top:258px;width:104px;height:31px;line-height:29px}
.arrow{width:30px;height:58px;background:var(--white);border:1px solid #ddd}
.arrow-l{left:93px;top:343px;border-radius:29px 0 0 29px;border-right:0}
.arrow-r{left:901px;top:343px;border-radius:0 29px 29px 0;border-left:0}
.arrow svg{position:absolute;top:21px}
.slider-shadow{left:140px;top:558px;width:745px;height:30px;background:radial-gradient(ellipse at 50% 0,rgba(0,0,0,.25),transparent 70%)}
.promo{top:610px;width:377px;height:109px;background:var(--white);overflow:hidden}
.promo-phone{left:17px;top:10px;width:86px;height:110px;border-radius:10px}
.promo h2{position:absolute;font:26px "Lobster",cursive;font-weight:400;white-space:nowrap}
.promo .rule{position:absolute;height:2px;background:var(--blue)}
.promo .caps{position:absolute;right:15px;top:56px;font:15px "Oswald",sans-serif;color:#555;white-space:nowrap}
.promo .more{position:absolute;right:15px;top:83px;font:13px "Lobster",cursive;color:var(--blue)}
.promo-pct{left:27px;top:14px;font:38px/36px "Lobster",cursive;color:var(--blue);text-align:center}
.sec-head{top:736px;width:377px;height:43px;background:#f3f3f3;border:1px solid #e3e3e3}
.sec-head h3{position:absolute;left:17px;top:9px;font:18px "Lobster",cursive;font-weight:400;color:#8a8a8a}
.sec-head .nb{position:absolute;top:13px;width:15px;height:15px;border:1px solid #ccc;background:#fafafa}
.card{top:786px;width:177px;height:274px;background:#f6f6f6;border:1px solid #e3e3e3}
.card .frame{position:absolute;left:14px;top:14px;width:146px;height:160px;background:var(--white)}
.card .ph{position:absolute;left:45px;top:25px;width:56px;height:110px;border-radius:7px}
.card .name{position:absolute;left:14px;top:184px;width:146px;font:300 11.5px/16px "Oswald",sans-serif;color:#666}
.card .rule{position:absolute;left:14px;top:222px;width:146px;height:1px;background:var(--line)}
.card .price{position:absolute;left:14px;top:228px;font:23px "Lobster",cursive;color:var(--blue)}
.footer{left:65px;top:1107px;width:895px;height:84px;background:linear-gradient(90deg,#e4e4e4,#f2f2f2 50%,#e4e4e4);border-top:1px solid #ddd}
.news{left:140px;top:1138px;font:16px "Lobster",cursive;color:#777;white-space:nowrap}
.news-input{left:333px;top:1134px;width:161px;height:31px;background:var(--white);border:1px solid #ddd}
.news-btn{left:497px;top:1134px;width:38px;height:31px;background:var(--yellow);border:1px solid var(--yellow-dark);border-radius:2px}
.info{white-space:nowrap}
.info b{display:block;font:15px "Lobster",cursive;font-weight:400;color:#777}
.info span{display:block;font:300 10px "Oswald",sans-serif;color:var(--blue)}
</style>
</head>
<body>
<div class="abs page"></div>
<div class="abs topline"></div>

<header>
  <div class="abs welcome">Default welcome msg!</div>
  <div class="abs currency"><span>Select Your Currency</span><div class="select">US Dollar - USD<i></i></div></div>
  <div class="abs logo">Appvault<br>depot</div>
  <nav class="abs account"><a href="#">MY ACCOUNT</a><a href="#">MY WISHLIST</a><a href="#">CHECKOUT</a><a href="#">LOG IN</a></nav>
  <div class="abs cart">
    <svg width="24" height="18" viewBox="0 0 24 18" fill="none" stroke="#fff" stroke-width="1.5"><path d="M2 6h20l-3 11H5z"/><path d="M7 6l3-5M17 6l-3-5M5 10h14M6 13h12"/></svg>
    <p>SHOPPING CART<br>You have no items in your shopping cart.</p>
  </div>
  <nav class="abs nav"><a href="#">Mobile Phones</a><a href="#">Smart Phones</a><a href="#">Communicators</a><a href="#">Accessories</a></nav>
  <div class="abs search">Search entire store here...</div>
  <div class="abs search-btn"><svg width="28" height="24" viewBox="0 0 28 24"><circle cx="13" cy="11" r="6" fill="none" stroke="#fff" stroke-width="2.5"/><path d="M17 15l5 5" stroke="#fff" stroke-width="3"/></svg></div>
  <div class="abs blueline"></div>
</header>

<section class="hero">
  <div class="abs slider-shadow"></div>
  <div class="abs slider"></div>
  <div class="abs slide"></div>
  <div class="abs photo phone-lg" role="img" aria-label="Smartphone product photo"></div>
  <svg class="abs badge" width="94" height="88" viewBox="0 0 94 88">
    <polygon fill="#f5b820" stroke="#d99a0c" points="47,2 56,14 71,8 73,24 89,27 82,41 92,53 77,59 79,75 63,73 55,87 44,76 30,84 27,68 11,66 17,52 4,42 17,32 13,17 29,17 33,3"/>
    <text x="47" y="53" text-anchor="middle" transform="rotate(-25 47 44)" font-family="Lobster,cursive" font-size="24" fill="#7a4e00">$395</text>
  </svg>
  <h1 class="abs hero-title" style="font-weight:400">Cras nulla</h1>
  <div class="abs hero-sub">In molestie urna id ipsum</div>
  <p class="abs hero-body">Etiam mollis nisi non diam facilisis pellentesque donec volutpat...</p>
  <div class="abs btn btn-hero">Click Here &#8250;</div>

  <div class="abs sale-panel"></div>
  <div class="abs sale-card">
    <div class="abs sale-word">Sale</div>
    <div class="abs sale-sub">Ut et tellus arcu, vestibulum molestie enim.</div>
    <div class="abs sale-off">50% Off</div>
    <p class="abs sale-body">Cras scelerisque risus sed risus sollicitudin placerat dictfsum augue condimentum donec volutpat velit et orci laoreet eu ullamcorper augue vehicula...</p>
    <div class="abs btn btn-shop">Shop Now! &#8250;</div>
  </div>
  <div class="abs arrow arrow-l"><svg style="left:8px" width="14" height="16"><path d="M11 1L3 8l8 7" fill="none" stroke="#bbb" stroke-width="3"/></svg></div>
  <div class="abs arrow arrow-r"><svg style="left:6px" width="14" height="16"><path d="M3 1l8 7-8 7" fill="none" stroke="#bbb" stroke-width="3"/></svg></div>
</section>

<section class="promos">
  <div class="abs promo" style="left:123px">
    <div class="abs photo promo-phone" role="img" aria-label="Smartphone product photo"></div>
    <h2 style="left:120px;top:12px;color:#111">Stream Dolor sit amet</h2>
    <div class="rule" style="left:120px;top:48px;width:242px"></div>
    <div class="caps">SAVE 10% OFF ON 3G PHONES</div>
    <div class="more">Learn more...</div>
  </div>
  <div class="abs promo" style="left:524px">
    <div class="abs promo-pct">25%<br>Off</div>
    <h2 style="left:109px;top:12px;color:var(--orange)">Use Your Credit Card..</h2>
    <div class="rule" style="left:109px;top:48px;width:252px"></div>
    <div class="caps">SAVE AT GRAVIDA VELIT AC INTERDUM</div>
    <div class="more">Lear more...</div>
  </div>
</section>

<section class="products">
  <div class="abs sec-head" style="left:122px"><h3>Mobile Phones</h3><i class="nb" style="left:321px"></i><i class="nb" style="left:344px"></i></div>
  <div class="abs sec-head" style="left:523px"><h3>Camera Phones</h3><i class="nb" style="left:322px"></i><i class="nb" style="left:345px"></i></div>

  <article class="abs card" style="left:122px"><div class="frame"><div class="photo ph" role="img" aria-label="Smartphone product photo"></div></div><p class="name">Mauris et dui id purus malesuada semper</p><div class="rule"></div><div class="price">$199.99</div></article>
  <article class="abs card" style="left:322px"><div class="frame"><div class="photo ph" role="img" aria-label="Smartphone product photo"></div></div><p class="name">Praesent pellentesque arcu feugiat elit</p><div class="rule"></div><div class="price">$150.00</div></article>
  <article class="abs card" style="left:523px"><div class="frame"><div class="photo ph" role="img" aria-label="Smartphone product photo"></div></div><p class="name">Fusce dignissim erat sit amet enim lobortis</p><div class="rule"></div><div class="price">$149.99</div></article>
  <article class="abs card" style="left:724px"><div class="frame"><div class="photo ph" role="img" aria-label="Smartphone product photo"></div></div><p class="name">Lorem ut mi gravida accumsan vestibulum</p><div class="rule"></div><div class="price">$349.99</div></article>
</section>

<footer>
  <div class="abs footer"></div>
  <div class="abs news">Sign Up for Our Newsletter:</div>
  <div class="abs news-input"></div>
  <div class="abs news-btn"><svg width="36" height="29" viewBox="0 0 36 29"><rect x="8" y="7" width="20" height="14" fill="#fff" stroke="#c78a00"/><path d="M8 7l10 8 10-8" fill="none" stroke="#c78a00"/></svg></div>
  <svg class="abs" style="left:565px;top:1135px" width="20" height="20" viewBox="0 0 20 20"><path d="M4 2l4 0 1 5-3 2c1 3 3 5 6 6l2-3 5 1v4c-8 1-16-7-15-15z" fill="#777"/></svg>
  <div class="abs info" style="left:589px;top:1136px"><b>+444 (2000) 654321</b></div>
  <div class="abs info" style="left:563px;top:1155px"><span>Monday to Saturday: 10:00am - 7:00pm</span></div>
  <svg class="abs" style="left:740px;top:1137px" width="36" height="18" viewBox="0 0 36 18"><rect x="0" y="2" width="22" height="11" fill="#777"/><path d="M22 5h8l5 5v3H22z" fill="#777"/><circle cx="7" cy="14" r="3" fill="#777" stroke="#eee"/><circle cx="28" cy="14" r="3" fill="#777" stroke="#eee"/></svg>
  <div class="abs info" style="left:781px;top:1136px"><b>Free Shipping</b></div>
  <div class="abs info" style="left:739px;top:1155px"><span>On Order Over $99:00</span></div>
</footer>
</body>
</html>
```